A parent Company needs a website as a leading diversified business in industrial Conglomerates in Af

Tesel Group is a private (Holding) limited liability company incorporated under the Companies Code, 1963 (Act 179) in November, 2013 to following the speedy growth in numbers of its current subsidiaries which has been founded several years ago with an emerging force to become one of the largest and a leading diversified business in industrial Conglomerates in Africa.
The Group which is 100% wholly owned indigenous Ghanaian Company focuses on provision of local, value-added products and services that meet the needs of the African population. The Group is headquartered in Accra, Ghana with interests across a range of sectors in Africa.
We are currently into Food & Beverage, Real Estate Development, Transportation, Health Care, Consumer Products Distribution, Agro Processing, Manufacturing, ICT, Exports & Import, and still counting.
In the next 3 years, we shall announce our ambitions to enter Ghana's largest Oil and Gas industry, playing a strategic role in the petroleum sector with strategic alliances, and help build Ghana's biggest and most important Energy sector in the country.
Inspired by billionaires Ned Forlow, Calvin Drossel, and Ubeni Sorkapa, Tesel Group (Tesel Foundation) is committed to making a name for itself on the philanthropic circuit and has given away privately and still given to the cause to the needy in the society and some specific social causes in Ghana.
The company is managed by a 5 member board and a 2 member advisory experts who are non-board members.
The company has a vision, mission and it is guided by its core values.
We would like to see a designs that is very professional and looks corporate and can attract investors and partners. It must communicate financial safety and growth and must reflect our logo colors.

```html
<!DOCTYPE html>
<html lang="en">
<head>
<meta charset="utf-8">
<title>Tesel Group</title>
<link href="https://fonts.googleapis.com/css2?family=Open+Sans:wght@400;600;700&display=swap" rel="stylesheet">
<style>
:root{
  --ink:#444;
  --muted:#777;
  --brand-blue:#1b75bb;
  --brand-red:#c8202a;
  --dark:#2e2e2e;
  --darker:#1e1e1e;
  --nav:#3a3a3a;
  --panel:#eeeeee;
  --line:#d9d9d9;
  --white:#fff;
}
*{box-sizing:border-box;margin:0;padding:0}
html,body{width:779px;height:1200px;overflow:hidden}
body{font-family:"Open Sans",Arial,sans-serif;color:var(--ink);background:#f4f4f4;position:relative;font-size:9px;line-height:1.45}
.wrap{width:729px;margin:0 auto;position:relative}

.topbar{height:20px;background:var(--darker);color:#ccc;font-size:8px}
.topbar .wrap{display:flex;justify-content:flex-end;align-items:center;height:20px;gap:8px}
.topbar .dot{width:8px;height:8px;border-radius:50%;background:#888}

.header{height:84px;background:var(--white)}
.header .wrap{display:flex;justify-content:space-between;align-items:center;height:84px}
.brand{display:flex;align-items:center;gap:8px}
.brand-mark{width:34px;height:34px;border-radius:50%;background:var(--brand-blue)}
.brand-name{font-weight:700;font-size:16px;color:var(--brand-blue);line-height:1.1}
.brand-tag{font-size:7px;color:var(--muted)}
.call{font-size:15px;font-weight:600;color:#333}

.nav{height:22px;background:var(--nav)}
.nav ul{list-style:none;display:flex;height:22px}
.nav li{color:#eee;font-size:8px;font-weight:600;padding:0 12px;line-height:22px;text-transform:uppercase}
.nav li.active{background:var(--brand-red)}

.hero{height:262px;background:linear-gradient(90deg,#f7f7f7 0%,#eef1f4 40%,#c9d3dc 65%,#8d9aa6 100%);position:relative}
.hero-photo{position:absolute;right:0;top:0;width:460px;height:262px;background:linear-gradient(120deg,rgba(255,255,255,0) 0%,rgba(120,135,150,.35) 60%,rgba(60,70,85,.45) 100%)}
.hero-copy{position:absolute;left:25px;top:44px;width:250px}
.hero-copy h1{color:var(--brand-blue);font-size:18px;font-weight:700;margin-bottom:8px}
.hero-copy p{font-size:8px;color:#555}
.btn{display:inline-block;background:var(--brand-red);color:#fff;font-size:8px;font-weight:600;padding:4px 10px;border-radius:2px;margin-top:10px}

.welcome{margin:26px auto 0;height:62px;background:var(--white);border-left:4px solid var(--brand-blue);display:flex;align-items:center;justify-content:space-between;padding:0 14px;box-shadow:0 1px 2px rgba(0,0,0,.1)}
.welcome h2{font-size:14px;font-weight:400;color:#333}
.welcome h2 b{color:var(--brand-blue);font-weight:600}
.welcome p{font-size:7.5px;color:var(--muted);width:400px}
.btn-dark{background:#4a4a4a;color:#fff;font-size:11px;font-weight:600;padding:6px 14px}

.section-head{display:flex;align-items:center;justify-content:space-between;height:28px;background:var(--white);margin-top:30px;padding:0 8px;box-shadow:0 1px 2px rgba(0,0,0,.08)}
.section-head h3{font-size:15px;font-weight:400;color:#333;display:flex;align-items:center;gap:6px}
.icon-sq{width:18px;height:18px;background:var(--brand-blue);border-radius:2px}
.arrows{display:flex;gap:2px}
.arrows span{width:12px;height:12px;background:#bbb;display:flex;align-items:center;justify-content:center}

.services{display:flex;justify-content:space-between;margin-top:18px}
.service{width:170px}
.service .photo{height:138px;border:1px solid var(--line)}
.service p{text-align:center;font-size:7.5px;font-weight:600;margin-top:8px;text-transform:uppercase;color:#555}
.p-estate{background:linear-gradient(#9fc1de,#5f7e98)}
.p-food{background:linear-gradient(#c2843f,#6e3d1a)}
.p-transport{background:linear-gradient(#cfd6df,#6d7888)}
.p-manufacturing{background:linear-gradient(#b8bec6,#4f5967)}

.lower{display:flex;justify-content:space-between;margin-top:34px}
.about{width:500px}
.about .section-head{margin-top:0;height:30px}
.about p{font-size:8px;color:#555;margin-top:12px;width:420px}
.private{width:190px;background:var(--white);box-shadow:0 1px 2px rgba(0,0,0,.1)}
.private .section-head{margin-top:0;height:30px;background:var(--panel);box-shadow:none}
.private .section-head h3{font-size:13px}
.private form{padding:10px}
.field{height:18px;border:1px solid var(--line);font-size:7px;color:#999;padding:3px 6px;margin-bottom:8px;background:#fafafa}
.btn-login{display:inline-block;background:#4a4a4a;color:#fff;font-size:8px;padding:4px 10px}

.partners{margin-top:22px;display:flex;gap:24px;align-items:center;padding-left:24px;height:40px}
.badge{width:90px;height:28px;background:#d6d6d6;border-radius:3px}
.badge.round{width:40px;border-radius:50%}
.partners-rule{height:12px;background:#dcdcdc;margin-top:8px}

.footer{position:absolute;left:0;top:990px;width:779px;height:185px;background:var(--dark);color:#bbb}
.footer .wrap{display:flex;justify-content:space-between;padding-top:18px}
.footer h4{color:#fff;font-size:9px;font-weight:600;margin-bottom:6px;display:flex;align-items:center;gap:5px}
.footer h4 i{width:9px;height:9px;background:var(--brand-blue);display:inline-block}
.footer ul{list-style:none;font-size:7.5px;line-height:1.6}
.f-links{width:150px}
.f-about{width:300px;font-size:7.5px}
.f-contact{width:150px;font-size:7.5px}
.f-contact .brand{margin-bottom:10px}
.f-contact .brand-name{color:#fff;font-size:12px}
.f-row{display:flex;gap:6px;align-items:flex-start;margin-bottom:5px}
.copyright{position:absolute;left:0;top:1175px;width:779px;height:25px;background:var(--darker);color:#aaa;font-size:7px;text-align:center;line-height:25px}
</style>
</head>
<body>
<div class="topbar"><div class="wrap"><span>Apply Now</span><span>|</span><span>Contact Us</span><span class="dot"></span><span class="dot"></span><span class="dot"></span><span class="dot"></span></div></div>

<header class="header"><div class="wrap">
  <div class="brand"><span class="brand-mark"></span><div><div class="brand-name">TESEL GROUP</div><div class="brand-tag">Diversity, Integrity &amp; Growth</div></div></div>
  <div class="call">Call Now: 800-555-0142</div>
</div></header>

<nav class="nav"><div class="wrap"><ul>
  <li class="active">Home</li><li>Real Estate Development</li><li>Food</li><li>Transportation</li><li>Manufacturing</li><li>About Us</li><li>Contact Us</li>
</ul></div></nav>

<section class="hero">
  <div class="hero-photo" role="img" aria-label="Business team meeting around a laptop in a bright office"></div>
  <div class="wrap"><div class="hero-copy">
    <h1>TESEL GROUP</h1>
    <p>Tesel Group is a private (Holding) limited liability company incorporated under the Companies Code, 1963 (Act 179) in November, 2013 to following the speedy growth in numbers of its current subsidiaries which has been founded several years ago with an emerging force to become one of the largest and a leading diversified business in industrial Conglomerates in Africa.</p>
    <span class="btn">Read More</span>
  </div></div>
</section>

<div class="wrap">
  <div class="welcome">
    <div>
      <h2>Welcome to <b>Tesel Group</b></h2>
      <p>Lorem Ipsum is simply dummy text of the printing and typesetting industry. Lorem Ipsum has been the industry's standard dummy text ever since the 1500s, when an unknown printer took a galley of type and scrambled it to make a type specimen book.</p>
    </div>
    <span class="btn-dark">READ MORE</span>
  </div>

  <div class="section-head">
    <h3><span class="icon-sq"></span>SERVICES</h3>
    <div class="arrows">
      <span><svg width="6" height="6" viewBox="0 0 6 6"><path d="M4 0L1 3l3 3" stroke="#fff" fill="none"/></svg></span>
      <span><svg width="6" height="6" viewBox="0 0 6 6"><path d="M2 0l3 3-3 3" stroke="#fff" fill="none"/></svg></span>
    </div>
  </div>

  <div class="services">
    <div class="service"><div class="photo p-estate" role="img" aria-label="Modern high-rise buildings"></div><p>Real Estate Development</p></div>
    <div class="service"><div class="photo p-food" role="img" aria-label="Plates of prepared food"></div><p>Food</p></div>
    <div class="service"><div class="photo p-transport" role="img" aria-label="Trucks and transport fleet"></div><p>Transportation</p></div>
    <div class="service"><div class="photo p-manufacturing" role="img" aria-label="Industrial manufacturing machinery"></div><p>Manufacturing</p></div>
  </div>

  <div class="lower">
    <div class="about">
      <div class="section-head"><h3><span class="icon-sq"></span>ABOUT US</h3></div>
      <p>Tesel Group is a private (Holding) limited liability company incorporated under the Companies Code, 1963 (Act 179) in November, 2013 to following the speedy growth in numbers of its current subsidiaries which has been founded several years ago with an emerging force to become one of the largest and a leading diversified business in industrial Conglomerates in Africa.</p>
      <span class="btn">Read More</span>
    </div>
    <div class="private">
      <div class="section-head"><h3><span class="icon-sq"></span>PRIVATE ACCESS</h3></div>
      <form>
        <div class="field">Enter your Username</div>
        <div class="field">Enter your Password</div>
        <span class="btn-login">Login</span>
      </form>
    </div>
  </div>

  <div class="partners">
    <span class="badge"></span><span class="badge round"></span><span class="badge"></span><span class="badge"></span>
  </div>
  <div class="partners-rule"></div>
</div>

<footer class="footer"><div class="wrap">
  <div class="f-links">
    <h4><i></i>Investments</h4>
    <ul><li>Home</li><li>Food</li><li>Real Estate Development</li><li>Transportation</li><li>Manufacturing</li></ul>
  </div>
  <div class="f-about">
    <h4><i></i>About Us</h4>
    <p>Tesel Group is a private (Holding) limited liability company incorporated under the Companies Code, 1963 (Act 179) in November, 2013 to following the speedy growth in numbers of its current subsidiaries which has been founded several years ago with an emerging force to become one of the largest and a leading diversified business in industrial Conglomerates in Africa.</p>
  </div>
  <div class="f-contact">
    <div class="brand"><span class="brand-mark"></span><div class="brand-name">TESEL GROUP</div></div>
    <div class="f-row"><svg width="8" height="10" viewBox="0 0 8 10"><path d="M4 0a4 4 0 0 1 4 4c0 3-4 6-4 6S0 7 0 4a4 4 0 0 1 4-4z" fill="#bbb"/></svg><span>742 Harbor Crest Lane<br>Suite 310</span></div>
    <div class="f-row"><svg width="8" height="8" viewBox="0 0 8 8"><path d="M1 0h2l1 2-1 1c.5 1 1 1.5 2 2l1-1 2 1v2c-4 0-8-4-8-7z" fill="#bbb"/></svg><span>Phone: (800) 555-0187</span></div>
    <div class="f-row"><svg width="8" height="8" viewBox="0 0 8 8"><rect x="0" y="1" width="8" height="6" fill="#bbb"/></svg><span>Fax: (800) 555-0188</span></div>
  </div>
</div></footer>
<div class="copyright">Copyright 2014 - All rights reserved</div>
</body>
</html>
```